Lorabelle Hair Flyer - tri-fold

I have added 2 participation payments to the project. I am not sure how I allocate them, but I would like to award them to two particular designers. When I find out how to do it I will allocate them. Thank you to everyone that participated, most designs were outstanding, and it was very hard to chose a winner.
========================================
PLEASE NO NEW DESIGNERS. I HAVE ENOUGH GOOD DESIGNS NOW, THAT I WILL WORK WITH ON THE EXISTING DESIGNERS. THANK YOU FOR ALL PARTICIPATING. THE QUALITY OF ALL SUBMISSIONS HAS EXCEEDED MY EXPECTATIONS, AND IS MAKING THE CHOICE DIFFICULT.
==============================================================

I have attached a proof pdf which is my draft design (I just used a stock template from Printorra) to do the mock up.

I would like you to replace the 3 main pictures of models with those I have attached. The name of the files will tell you where they should go.
I have attached pictures of all the stock photos as well, and most of the text is in the text file to save you typing it in.

I want the background colour to match Lorabelle colours so black with a fade to gold or something like that, must look sophisticated. I have attached Lorabelle logo files in black and white background.

The main pictures I have attached from the models will need to be blended into the background as well, but the hair still needs to be visible (might be hard given it is black hair as well,). The title stripes should be a gold fade as well, and the lorabelle text should be replaced with our logo.

please also add in the Facebook and WhatsApp logo's in the appropriate places. The dimensions should be 279mm * 216mm and print in the PrintOrra tri-fold brochure.

Possible ongoing work for the winning person, as the original designer of the logo only does logos/business cards, not other print material. Have logos in other formats (ai/cdr/jpeg) if required

Target Market(s)

African women

Industry/Entity Type

Hair

Font styles to use
Serif

Requirements
Must have
• Logo, product pictures, attached text, layout changes to draft mock up is ok if it looks better. Must conform to Printorra tri-fold layout
Nice to have
• Based on logo colours, black, white, gold complimentary colours to that palette are ok

```html
<!DOCTYPE html>
<html lang="en">
<head>
<meta charset="utf-8">
<title>Lorabelle Hair – Tri-fold Flyer</title>
<link rel="stylesheet" href="https://fonts.googleapis.com/css2?family=Open+Sans:wght@400;600;700&display=swap">
<style>
  :root {
    --page-bg: #f2f2f2;
    --black: #050403;
    --gold: #c9a24a;
    --gold-light: #e2c478;
    --gold-deep: #8a6a2a;
    --white: #ffffff;
    --ink: #141008;
  }
  * { box-sizing: border-box; margin: 0; padding: 0; }
  html, body {
    width: 1200px; height: 991px; overflow: hidden;
    background: var(--page-bg);
    font-family: "Open Sans", Arial, sans-serif;
  }
  .brochure {
    position: absolute; left: 50px; top: 70px;
    width: 1100px; height: 852px; overflow: hidden;
    background: linear-gradient(180deg, var(--gold) 0%, var(--gold-deep) 18%, #2a1c10 45%, var(--black) 75%);
    box-shadow: 0 10px 30px rgba(0,0,0,.25);
  }
  .model-photo {
    position: absolute; left: 170px; top: 60px; width: 740px; height: 700px;
    border-radius: 50%;
    background: radial-gradient(ellipse at 50% 45%, rgba(110,70,40,.85) 0%, rgba(70,44,26,.7) 35%, rgba(30,20,12,.4) 60%, rgba(0,0,0,0) 75%);
  }
  .fold { position: absolute; top: 0; width: 1px; height: 100%; background: rgba(255,255,255,.08); }
  .fold--one { left: 366px; } .fold--two { left: 733px; }

  .section-title {
    position: absolute; left: 0; top: 70px; width: 366px; height: 78px;
    background: linear-gradient(90deg, var(--gold) 0%, var(--gold-light) 55%, rgba(201,162,74,.6) 100%);
    text-align: center; color: var(--white); padding-top: 6px;
  }
  .section-title h2 { font-size: 27px; font-weight: 700; }
  .section-title p { font-size: 13px; line-height: 1.2; }

  .product { position: absolute; width: 230px; }
  .product__photo {
    width: 112px; height: 112px; border-radius: 50%;
    border: 4px solid var(--gold);
    background: radial-gradient(circle at 50% 50%, #1a1a1a 0%, #3a3a3a 45%, #f2f2f2 70%);
  }
  .product__label {
    margin-top: 4px; height: 40px; line-height: 40px; padding-left: 26px;
    font-size: 22px; font-weight: 700; color: var(--ink); white-space: nowrap;
    background: linear-gradient(90deg, rgba(201,162,74,0) 0%, var(--gold) 35%, var(--gold-light) 100%);
  }
  .product__label--two-line { height: 56px; line-height: 24px; padding-top: 4px; text-align: center; padding-left: 40px; }
  .product--right .product__photo { margin-left: 100px; }

  .product--straight { left: 40px; top: 165px; }
  .product--body-wave { left: 136px; top: 320px; }
  .product--deep-wave { left: 40px; top: 495px; }
  .product--fumi-curl { left: 136px; top: 655px; }
  .product--romance-curl { left: 380px; top: 30px; }
  .product--kinky-curl { left: 503px; top: 190px; }
  .product--jerry-curl { left: 380px; top: 370px; }
  .product--closures { left: 503px; top: 530px; }

  .frontal-note {
    position: absolute; left: 390px; top: 770px; width: 330px;
    color: var(--gold-light); font-size: 18px; font-weight: 600; text-align: right;
  }

  .ranges {
    position: absolute; left: 760px; top: 230px; width: 300px;
    color: var(--white); text-align: center; font-size: 14px; line-height: 1.4;
  }
  .ranges h2 { font-size: 22px; font-weight: 700; margin-bottom: 2px; }
  .ranges p { margin-bottom: 18px; }

  .brand {
    position: absolute; left: 760px; top: 600px; width: 300px;
    text-align: center; color: var(--white);
  }
  .brand__mark { width: 34px; height: 34px; border-radius: 50%; background: var(--gold); margin: 0 auto 10px; }
  .brand__name { font-size: 36px; font-weight: 400; letter-spacing: 2px; }
  .brand__tag { font-size: 13px; font-weight: 400; }
</style>
</head>
<body>
  <main class="brochure">
    <div class="model-photo" role="img" aria-label="Photo of a smiling model with voluminous curly hair, blended into the background"></div>
    <div class="fold fold--one"></div>
    <div class="fold fold--two"></div>

    <header class="section-title">
      <h2>Our Products</h2>
      <p>We provide natural 100g wefts in the<br>following styles</p>
    </header>

    <div class="product product--straight">
      <div class="product__photo" role="img" aria-label="Straight hair bundle"></div>
      <div class="product__label">Straight</div>
    </div>
    <div class="product product--right product--body-wave">
      <div class="product__photo" role="img" aria-label="Body wave hair bundles"></div>
      <div class="product__label">Body Wave</div>
    </div>
    <div class="product product--deep-wave">
      <div class="product__photo" role="img" aria-label="Deep wave hair bundles"></div>
      <div class="product__label">Deep Wave</div>
    </div>
    <div class="product product--right product--fumi-curl">
      <div class="product__photo" role="img" aria-label="Fumi curl hair bundles"></div>
      <div class="product__label">Fumi Curl</div>
    </div>

    <div class="product product--romance-curl">
      <div class="product__photo" role="img" aria-label="Romance curl hair bundles"></div>
      <div class="product__label">Romance Curl</div>
    </div>
    <div class="product product--right product--kinky-curl">
      <div class="product__photo" role="img" aria-label="Kinky curl hair bundles"></div>
      <div class="product__label">Kinky Curl</div>
    </div>
    <div class="product product--jerry-curl">
      <div class="product__photo" role="img" aria-label="Jerry curl hair bundles"></div>
      <div class="product__label">Jerry Curl</div>
    </div>
    <div class="product product--right product--closures">
      <div class="product__photo" role="img" aria-label="Body wave lace closure"></div>
      <div class="product__label product__label--two-line">Matching<br>Closures</div>
    </div>

    <p class="frontal-note">We also sell 360 Frontal Closures</p>

    <section class="ranges">
      <h2>Ranges</h2>
      <p>We have two ranges to give our customers choice, our Platinum range is sourced from India and comes from a single donor.</p>
      <p>Our Premium range is sourced from donors from Asia and are typically referred to as Brazilian or Peruvian in the Industry.</p>
      <p>Both are 100% Virgin Remy hair. Both come with a 1 year Warranty, both are the highest quality hair in the industry</p>
    </section>

    <div class="brand">
      <div class="brand__mark"></div>
      <div class="brand__name">LORABELLE</div>
      <div class="brand__tag">100% Human Hair</div>
    </div>
  </main>
</body>
</html>
```